Real EState

A real estate company. I want to start a mailing of 1,000 standard size post cards. I want to mail these every month. Starting Jan 2015. The first 1,000 talking about this new year, the following months something to do with the seasons or holidays upcoming. I would like the design to be familiar each month so that my company will be recognized. I can send you my business card and logo which has my address phone# etc. I only want to spend the $29 design change each month, not the $180. I believe this should be attainable knowing I want consistency, I want my clients to easily know who my company is and I am available to help them get their real estate needs accomplished. One phrase I would like them to read each time is this. Why don't you take this opportunity now and give me a call or stop by because " When you open our door, it will definitely open doors for you.

I am not good at this type communication. I would really like to speak to someone. I know we cannot so please bare with me. I have no idea if my brief has gone out to everyone or not. here is what I would like. My logo needs to be there. The letters K&R PROPERTIES needs to be in gold. The buildings and lines going across need to be a light gray. I would like to see a nice quality door along with maybe a side light window. There needs to be a key in the door. I would like to see the door opening. I also want the phrase that I sent to everyone regarding opening the door. All other colors need to blend in with the colors of the logo. Lets put in all the phone numbers on the business card along with the e-mail address. Please at this time leave off the web address until I can update the site.

Reason: I am not good at this kind of communication. My computer skills are not good enough to even understand the programs your using. I don't even know if everyone is getting my explanations or even the feed back. Every time I try to bring up a design I lose the page in front of me I think I am getting better working your system but time will tell. Please bare with me. I will be loyal to the designer that can give what I need but again I'm having a hard time knowing who's who and keeping track of them.

Industry/Entity Type

Real Estate

```html
<!DOCTYPE html>
<html lang="en">
<head>
<meta charset="utf-8">
<title>K&amp;R Properties Postcards</title>
<link rel="stylesheet" href="https://fonts.googleapis.com/css2?family=Roboto:ital,wght@0,300;0,400;1,500&display=swap">
<style>
  :root {
    --backdrop: #9ac8dd;
    --red: #df2b19;
    --orange: #ee8c00;
    --navy: #170f35;
    --gray: #9d9e95;
    --gold: #f0a02c;
    --white: #ffffff;
  }
  * { margin: 0; padding: 0; box-sizing: border-box; }
  html, body { width: 1200px; height: 1000px; overflow: hidden; }
  body {
    background: var(--backdrop);
    font-family: "Roboto", Arial, sans-serif;
    position: relative;
  }
  .postcard {
    position: absolute;
    width: 546px;
    height: 419px;
    overflow: hidden;
    box-shadow: 0 2px 8px rgba(0,0,0,0.18);
  }
  .postcard--red { left: 86px; top: 48px; background: var(--red); z-index: 3; }
  .postcard--orange { left: 328px; top: 290px; background: var(--orange); z-index: 2; }
  .postcard--navy { left: 576px; top: 538px; background: var(--navy); z-index: 1; }

  .dot-texture {
    position: absolute;
    left: 2px; top: 4px;
    width: 342px; height: 44px;
  }
  .postcard--red .dot-texture { background: rgba(90,20,20,0.12); }
  .postcard--orange .dot-texture,
  .postcard--navy .dot-texture { background: rgba(255,255,255,0.08); }

  .slogan {
    position: absolute;
    left: 19px; top: 103px;
    font-size: 22px;
    font-weight: 300;
    line-height: 30px;
    text-transform: uppercase;
    letter-spacing: -0.4px;
    white-space: nowrap;
  }
  .slogan em { font-style: italic; font-weight: 500; }
  .postcard--red .slogan { color: var(--white); }
  .postcard--orange .slogan { color: var(--navy); }
  .postcard--navy .slogan { color: var(--gold); }

  .divider {
    position: absolute;
    left: 340px; top: 104px;
    height: 210px;
    border-left: 3px dotted;
  }
  .postcard--red .divider { border-color: #5a1a22; }
  .postcard--orange .divider,
  .postcard--navy .divider { border-color: rgba(255,255,255,0.75); }

  .contact {
    position: absolute;
    left: 370px; top: 103px;
    width: 172px;
    font-size: 15px;
    font-weight: 300;
    line-height: 20px;
    white-space: nowrap;
  }
  .contact__name, .contact__title { display: block; }
  .contact__email { display: block; font-size: 11px; line-height: 16px; }
  .contact__address { margin-top: 14px; }
  .contact__phones { margin-top: 11px; }
  .postcard--red .contact { color: var(--white); }
  .postcard--red .contact__name,
  .postcard--red .contact__title,
  .postcard--red .contact__email { color: var(--gold); }
  .postcard--orange .contact { color: var(--navy); }
  .postcard--navy .contact { color: var(--white); }
  .postcard--navy .contact__name,
  .postcard--navy .contact__title,
  .postcard--navy .contact__email { color: var(--gold); }

  .footer-band {
    position: absolute;
    left: 0; bottom: 0;
    width: 100%; height: 80px;
    display: flex;
    align-items: center;
    padding-left: 181px;
    gap: 40px;
  }
  .postcard--red .footer-band { background: var(--navy); }
  .postcard--orange .footer-band,
  .postcard--navy .footer-band { background: var(--gray); }

  .partner-badge { width: 73px; height: 33px; display: block; }
  .brand-name {
    font-weight: 400;
    font-size: 15px;
    line-height: 20px;
    white-space: nowrap;
  }
  .postcard--red .brand-name { color: var(--gold); }
  .postcard--orange .brand-name,
  .postcard--navy .brand-name { color: var(--navy); }
</style>
</head>
<body>

<section class="postcard postcard--red">
  <div class="dot-texture" role="img" aria-label="Dot grid texture"></div>
  <p class="slogan"><em>Why don't</em> you take<br>this opportunity now<br>and give me a call or<br>stop by <em>because</em> "<br>when you open our<br>door, it will definitely<br>open doors for you.</p>
  <div class="divider"></div>
  <div class="contact">
    <span class="contact__name">Dale W. Harmon Jr.</span>
    <span class="contact__title">Broker &amp; Consultant</span>
    <span class="contact__email">daleharmon@kr-properties.com</span>
    <p class="contact__address">415 N. Maple<br>Crest Rd. Brookfield,<br>MI 48210</p>
    <p class="contact__phones">Office: 555.201.4514<br>Cell: 555.340.3517<br>Fax: 555.201.4518</p>
  </div>
  <div class="footer-band">
    <svg class="partner-badge" viewBox="0 0 73 33" role="img" aria-label="Partner listing badge"><rect x="1" y="1" width="71" height="31" fill="none" stroke="#f0a02c" stroke-width="1.5"/></svg>
    <span class="brand-name">K&amp;R PROPERTIES</span>
  </div>
</section>

<section class="postcard postcard--orange">
  <div class="dot-texture" role="img" aria-label="Dot grid texture"></div>
  <p class="slogan"><em>Why don't</em> you take<br>this opportunity now<br>and give me a call or<br>stop by <em>because</em> "<br>when you open our<br>door, it will definitely<br>open doors for you.</p>
  <div class="divider"></div>
  <div class="contact">
    <span class="contact__name">Dale W. Harmon Jr.</span>
    <span class="contact__title">Broker &amp; Consultant</span>
    <span class="contact__email">daleharmon@kr-properties.com</span>
    <p class="contact__address">415 N. Maple<br>Crest Rd. Brookfield,<br>MI 48210</p>
    <p class="contact__phones">Office: 555.201.4514<br>Cell: 555.340.3517<br>Fax: 555.201.4518</p>
  </div>
  <div class="footer-band">
    <svg class="partner-badge" viewBox="0 0 73 33" role="img" aria-label="Partner listing badge"><rect x="1" y="1" width="71" height="31" fill="none" stroke="#170f35" stroke-width="1.5"/></svg>
    <span class="brand-name">K&amp;R PROPERTIES</span>
  </div>
</section>

<section class="postcard postcard--navy">
  <div class="dot-texture" role="img" aria-label="Dot grid texture"></div>
  <p class="slogan"><em>Why don't</em> you take<br>this opportunity now<br>and give me a call or<br>stop by <em>because</em> "<br>when you open our<br>door, it will definitely<br>open doors for you.</p>
  <div class="divider"></div>
  <div class="contact">
    <span class="contact__name">Dale W. Harmon Jr.</span>
    <span class="contact__title">Broker &amp; Consultant</span>
    <span class="contact__email">daleharmon@kr-properties.com</span>
    <p class="contact__address">415 N. Maple<br>Crest Rd. Brookfield,<br>MI 48210</p>
    <p class="contact__phones">Office: 555.201.4514<br>Cell: 555.340.3517<br>Fax: 555.201.4518</p>
  </div>
  <div class="footer-band">
    <svg class="partner-badge" viewBox="0 0 73 33" role="img" aria-label="Partner listing badge"><rect x="1" y="1" width="71" height="31" fill="none" stroke="#170f35" stroke-width="1.5"/></svg>
    <span class="brand-name">K&amp;R PROPERTIES</span>
  </div>
</section>

</body>
</html>
```